I need a business card designed using the logo provided either vertical or horizontal......Crestmoor Property Partners is an Australian based real estate company that caters for the upper end of the market so the design of the business card "must reflect" the companies image!!
Colour combinations are optional but "must be realistic" and must be able to be accurately useable CMYK colours.
Please consider that any colours used "must be able to be used" and be suitable in following designs for "pull out banner signs" and "real estate signs".
The colours and the font in the attached designs are for example and other combinations are encouraged.
Target Market(s)
The High End of the Australian real estate market
Industry/Entity Type
Business
Contact Information for Business Card
Logo - Business Name - Director + Licensed Real Estate Agent - Mobile Number (Cell Phone) - Business Number - Fax - Email Address - Web address
Requirements
Must have
- Designs and colours (CMYK) that can easily be interpreted by an Australian printer.
Nice to have
- Some alternative ideas on colour and font..........the ones provided are ok and have been provided as an example but I am looking for alternative ideas
Should not have
- Loud, overly bright colours. Designs that do not reflect the professional standards of the business.
- Designs that look good on a computer monitor but can not be re-created on a printing press.............this is most important when it comes to shading etc.

```html
<!DOCTYPE html>
<html lang="en">
<head>
<meta charset="utf-8">
<title>Crestmoor Property Partners – Business Card</title>
<link href="https://fonts.googleapis.com/css2?family=Source+Sans+3:wght@400;600&display=swap" rel="stylesheet">
<style>
  :root {
    --backdrop: #e9e7e4;
    --card: #ffffff;
    --brand-blue: #1a64ad;
    --rule-blue: #1d74c0;
    --band-grey: #646466;
    --text-grey: #48484a;
    --text-light: #ffffff;
  }
  * { margin: 0; padding: 0; box-sizing: border-box; }
  html, body {
    width: 1200px; height: 1000px; overflow: hidden;
    background: var(--backdrop);
    font-family: "Source Sans 3", "Helvetica Neue", Arial, sans-serif;
  }
  .business-card {
    position: absolute; left: 220px; top: 274px;
    width: 756px; height: 450px;
    background: var(--card);
    overflow: hidden;
  }
  .footer-rule {
    position: absolute; left: 0; right: 0; top: 362px;
    height: 4px; background: var(--rule-blue);
  }
  .footer-band {
    position: absolute; left: 0; right: 0; top: 372px; bottom: 0;
    background: var(--band-grey);
  }
  .brand {
    position: absolute; left: 40px; top: 92px;
    display: flex; align-items: center; gap: 14px;
  }
  .brand-square { width: 26px; height: 26px; background: var(--brand-blue); }
  .brand-name {
    color: var(--brand-blue); font-weight: 600; font-size: 31px;
    letter-spacing: 0.3px;
  }
  .contact-list {
    position: absolute; left: 38px; top: 252px;
    list-style: none; color: var(--text-grey); font-size: 18px; line-height: 23px;
  }
  .contact-list li { display: flex; align-items: center; gap: 8px; }
  .contact-icon { width: 14px; height: 14px; fill: var(--brand-blue); }
  .agent {
    position: absolute; right: 36px; top: 236px; text-align: right;
    color: var(--text-grey); font-size: 18px; line-height: 23px;
  }
  .agent-name { color: var(--brand-blue); font-weight: 600; font-size: 21px; line-height: 26px; }
  .website {
    position: absolute; right: 36px; top: 398px;
    color: var(--text-light); font-size: 17px;
  }
</style>
</head>
<body>
  <div class="business-card">
    <div class="footer-rule"></div>
    <div class="footer-band"></div>

    <div class="brand">
      <span class="brand-square"></span>
      <span class="brand-name">Crestmoor Property Partners</span>
    </div>

    <ul class="contact-list">
      <li>
        <svg class="contact-icon" viewBox="0 0 14 14"><path d="M4 0h6a1 1 0 0 1 1 1v12a1 1 0 0 1-1 1H4a1 1 0 0 1-1-1V1a1 1 0 0 1 1-1zm1 2v6h4V2zm1 8v2h2v-2z"/></svg>
        <span>+ 999 999 9999</span>
      </li>
      <li>
        <svg class="contact-icon" viewBox="0 0 14 14"><path d="M3 1l2 3-1.3 1.5c.8 1.8 2.2 3.3 4 4.2L9.3 8.5l3 2-1 2.5C6 12.5 1.5 8 1 3z"/></svg>
        <span>+ 999 999 9999</span>
      </li>
      <li>
        <svg class="contact-icon" viewBox="0 0 14 14"><path d="M3 1h8v3H3zM1 5h12v6h-2V9H3v2H1zm3 5h6v4H4z"/></svg>
        <span>+ 999 999 9999</span>
      </li>
      <li>
        <svg class="contact-icon" viewBox="0 0 14 14"><path d="M0 3h14v9H0zm1 1.2V11h12V4.2L7 8.5z"/></svg>
        <span>info@crestmoorpp.com</span>
      </li>
    </ul>

    <div class="agent">
      <p class="agent-name">Daniel R. Hayes</p>
      <p class="agent-role">Director</p>
      <p class="agent-licence">Licensed Real Estate Agent</p>
    </div>

    <p class="website">www.crestmoorpp.com</p>
  </div>
</body>
</html>
```